Vesna Architecture

We are a architectural design and build company working between scales 1/1000 to 1/1 we want people to understand our difference from our design experience and quality.we build hotels restourants and office spaces.Our company name is Vesna architecture to mind sustainability.

We want to write our adress phone and work spesifications on the card and we want our logo as backround.

Ps:you could find the logo adress and phone box numbers from the web:www.vesnayapi.example

Target Market(s)

Who looks for experts.

Industry/Entity Type

Architecture

Requirements
Must have
• Design is over everything.
Should not have
• we don want it to be colorfull

```html
<!DOCTYPE html>
<html lang="tr">
<head>
<meta charset="utf-8">
<title>Vesna Mimarlık – Business Card</title>
<link rel="stylesheet" href="https://fonts.googleapis.com/css2?family=Barlow:wght@400;600&display=swap">
<style>
  :root {
    --bg: #e4e4e4;
    --card-light: #ffffff;
    --card-dark: #050505;
    --ink-dark: #111111;
    --ink-light: #f2f2f2;
    --mark-faint: #2e2e2e;
  }
  * { margin: 0; padding: 0; box-sizing: border-box; }
  html, body {
    width: 1200px;
    height: 920px;
    overflow: hidden;
    background: var(--bg);
    font-family: "Barlow", Arial, sans-serif;
  }
  .stage { position: relative; width: 1200px; height: 920px; }

  .card { position: absolute; }

  .card--front {
    left: 124px; top: 144px;
    width: 412px; height: 256px;
    background: var(--card-light);
  }
  .brand {
    position: absolute;
    left: 140px; top: 262px;
    color: var(--ink-dark);
    font-weight: 400;
    line-height: 1;
  }
  .brand__name { display: block; font-size: 100px; letter-spacing: -2px; }
  .brand__sub { display: block; font-size: 23px; letter-spacing: 3px; margin: 6px 0 0 36px; }

  .card--back {
    left: 504px; top: 396px;
    width: 416px; height: 388px;
    background: var(--card-dark);
    color: var(--ink-light);
  }
  .holder { position: absolute; left: 62px; top: 120px; }
  .holder__name { font-size: 16px; font-weight: 600; letter-spacing: 0.3px; }
  .holder__role { font-size: 15px; font-weight: 400; margin-top: 2px; }

  .back-mark { position: absolute; left: 62px; top: 172px; }

  .contact {
    position: absolute; left: 62px; top: 244px;
    font-size: 15px; line-height: 22px; font-weight: 400;
    list-style: none; letter-spacing: 0.2px;
  }
  .contact b { font-weight: 600; }
</style>
</head>
<body>
<main class="stage">
  <section class="card card--front" aria-label="Business card front"></section>
  <h1 class="brand">
    <span class="brand__name">vesna</span>
    <span class="brand__sub">MİMARLIK</span>
  </h1>

  <section class="card card--back" aria-label="Business card back">
    <div class="holder">
      <p class="holder__name">Deniz Arkan YILMAZ</p>
      <p class="holder__role">Mimar</p>
    </div>
    <svg class="back-mark" width="60" height="60" viewBox="0 0 60 60" aria-hidden="true">
      <circle cx="30" cy="30" r="26" fill="none" stroke="var(--mark-faint)" stroke-width="6"/>
    </svg>
    <ul class="contact">
      <li>Ardic Mah. Lale Cad. Kuyu Sok.</li>
      <li>No: 7 Besiktas / ISTANBUL</li>
      <li><b>t.</b> 0212 555 01 47</li>
      <li><b>f.</b> 0212 555 01 48</li>
      <li><b>e.</b>studio@vesnayapi.example</li>
    </ul>
  </section>
</main>
</body>
</html>
```